Business Card Design for Event Planning Company

Create a business card for event planning company using our new logo. After I pick the design, I will need files made for 6 employees. Our company provides event design & logistics services as well as venue management. The font should be sans serif and complementary to the logo. I will need to know the name of the font selected for the final design. The phone numbers listed should be separated by "." not "-"

Address for the card
PO Box 318, Washington, DC 20019

Card One
Lorna Pettibone
lpettibone@galavoyant.com
202.481.7730

Card Two
Miriam Okonkwo
mokonkwo@galavoyant.com
202.556.2047

Card Three
Tessa Varnholt
tvarnholt@galavoyant.com
978.620.4471

Card Four
Robin Fess
rfess@galavoyant.com
202.718.3362

Card Five
Ada-Rose Pelletan-Uzor
adarose@galavoyant.com
202.839.1205

Card Six
Beatrix Holloway
Beatrix@galavoyant.com
202.492.6618

Target Market(s)

Corporate/Non-Profit

Industry/Entity Type

Event Planning

Contact Information for Business Card

Address for the card

Card One
Lorna Pettibone
lpettibone@galavoyant.com
202.481.7730

Card Two
Miriam Okonkwo
202.556.2047

Card Three
Tessa Varnholt
978.620.4471

Card Four
Robin Fess
rfess@galavoyant.com
202.718.3362

Card Five
Ada-Rose Pelletan-Uzor
202.839.1205

Card Six
Beatrix Holloway
202.492.6618

Font styles to use
Sans Serif

Colors

Designer to choose colors to be used in the design.

Requirements
Must have
• Two-sided with logo
Should not have
• Extra colors or be too busy

```html
<!DOCTYPE html>
<html lang="en">
<head>
<meta charset="utf-8">
<title>Galavoyant Business Card</title>
<link href="https://fonts.googleapis.com/css2?family=Questrial&family=Didact+Gothic&display=swap" rel="stylesheet">
<style>
  :root {
    --teal: #5ba6a4;
    --teal-dark: #3f8c8a;
    --ink: #1d1d1d;
    --grey: #6d6d6d;
    --paper: #ffffff;
    --stage: #d9dadb;
    --band: #0c0c0c;
  }
  * { box-sizing: border-box; margin: 0; padding: 0; }
  html, body {
    width: 1200px; height: 889px; overflow: hidden;
    background: var(--stage);
    font-family: "Questrial", "Didact Gothic", sans-serif;
  }
  .canvas {
    position: relative; width: 1200px; height: 889px;
    display: flex; align-items: center; justify-content: center; gap: 40px;
  }
  .card {
    position: relative; width: 525px; height: 300px; overflow: hidden;
    box-shadow: 0 6px 18px rgba(0,0,0,.18);
  }

  /* Front side */
  .card-front { background: var(--paper); }
  .card-front .frame {
    position: absolute; inset: 12px; border: 1px solid #e2e2e2;
  }
  .wordmark {
    font-family: "Questrial", sans-serif; color: var(--teal-dark);
    font-size: 34px; letter-spacing: .5px; line-height: 1;
  }
  .card-front .wordmark { position: absolute; left: 300px; top: 92px; }
  .card-front .mark-dot {
    position: absolute; left: 372px; top: 58px; width: 24px; height: 24px;
    border-radius: 50%; background: var(--teal);
  }
  .holder-name {
    position: absolute; left: 34px; top: 182px; width: 196px;
    color: var(--teal); font-size: 20px; font-weight: 400;
    line-height: 1.2; white-space: nowrap;
  }
  .holder-name .surname { font-weight: 700; }
  .contact-list {
    position: absolute; left: 240px; top: 180px; width: 270px; list-style: none;
    color: var(--grey); font-size: 12.5px;
  }
  .contact-list li { display: flex; align-items: center; gap: 8px; height: 26px; white-space: nowrap; }
  .contact-list svg { width: 13px; height: 13px; fill: var(--teal); flex: none; }

  /* Back side */
  .card-back { background: var(--teal); }
  .card-back .frame {
    position: absolute; left: 12px; top: 12px; right: 12px; bottom: 12px;
    border: 1.5px solid rgba(20,60,60,.45);
  }
  .card-back .band {
    position: absolute; left: 0; right: 0; bottom: 0; height: 92px; background: var(--band);
  }
  .card-back .band::before {
    content: ""; position: absolute; left: 0; right: 0; top: 0; height: 2px; background: #fff;
  }
  .logo-tab {
    position: absolute; left: 50%; bottom: 46px; transform: translateX(-50%);
    width: 250px; height: 84px; background: var(--paper);
    clip-path: polygon(7% 0, 93% 0, 100% 50%, 93% 100%, 7% 100%, 0 50%);
    display: flex; flex-direction: column; align-items: center; justify-content: center; gap: 6px;
  }
  .logo-tab .mark-dot {
    width: 20px; height: 20px; border-radius: 50%; background: var(--teal);
  }
  .logo-tab .wordmark { font-size: 28px; }
</style>
</head>
<body>
<main class="canvas">
  <section class="card card-front" aria-label="Business card front">
    <div class="frame"></div>
    <span class="mark-dot"></span>
    <div class="wordmark">galavoyant</div>
    <h1 class="holder-name">LORNA <span class="surname">PETTIBONE</span></h1>
    <ul class="contact-list">
      <li>
        <svg viewBox="0 0 16 16" aria-hidden="true"><path d="M1 3h14v10H1z M2 4l6 5 6-5" fill="none" stroke="#5ba6a4" stroke-width="1.6"/></svg>
        lpettibone@galavoyant.com
      </li>
      <li>
        <svg viewBox="0 0 16 16" aria-hidden="true"><path d="M3 1h3l1 4-2 1c1 2 3 4 5 5l1-2 4 1v3c0 1-1 2-2 2C7 15 1 9 1 3c0-1 1-2 2-2z"/></svg>
        202.481.7730
      </li>
      <li>
        <svg viewBox="0 0 16 16" aria-hidden="true"><path d="M8 1a5 5 0 0 1 5 5c0 4-5 9-5 9S3 10 3 6a5 5 0 0 1 5-5zm0 3a2 2 0 1 0 0 4 2 2 0 0 0 0-4z"/></svg>
        PO Box 318, Washington, DC 20019
      </li>
    </ul>
  </section>

  <section class="card card-back" aria-label="Business card back">
    <div class="frame"></div>
    <div class="band"></div>
    <div class="logo-tab">
      <span class="mark-dot"></span>
      <div class="wordmark">galavoyant</div>
    </div>
  </section>
</main>
</body>
</html>
```